"Thank You" card for professional property management agency.

We need to create a DL size "Thank You" card primarily used to thank new clients for their business and referrals.
We are a real estate agency based on Sydney's Northern Beaches. We want the card to feel happy and professional, incorporating our logo.
See our website for details about our business - www.harbourlanerealty.com.au
We have attached our logo in black text and white text as well as some images we have used across our website.
One side must have the ability to hand write a message of thank you on.
I would like this to be a clean and simple design, feel free to use any image supplied, but we are also happy with plain or patterned designs too.

Target Market(s)

Property investors male and female aged 30-60

Industry/Entity Type

Real Estate

Font styles to use
Other font styles liked:
• Please let the designer choose font

Colors

Designer to choose colors to be used in the design.

Requirements
Must have
• DL Size: Full Bleed 213x102mm. Doc size 210x99mm (horizontal)
• Harbour Lane Realty Logo
• Contact Details:
• info@harbourlanerealty.com.au
• Tel: 0493 716 258
• Suite 6, 17 Wentmore Rd, Calderwood NSW 2187
• "Thank You" somewhere on the card
• Area or side to write message on.
• Design to be provided in editable photoshop PSD file and print ready PDF file
Nice to have
• Sleek professional design that feels "happy or grateful" as it is a thank you card
• Happy to use a plain colour or pattern on one side - it does not have to be an image provided, but feel free to design with either.
Should not have
• should not be too busy, keep it clean and simple.

```html
<!DOCTYPE html>
<html lang="en">
<head>
<meta charset="utf-8">
<title>Harbour Lane Realty – Thank You Card</title>
<link href="https://fonts.googleapis.com/css2?family=Raleway:wght@500;600;700&display=swap" rel="stylesheet">
<style>
  :root {
    --page-bg: #e4e6e8;
    --card-white: #ffffff;
    --card-fade: #eceeef;
    --teal: #1b8e9c;
    --ink: #3a3f44;
    --sky: #9fc6dc;
    --sea: #2f6f95;
    --foliage: #7d8f5c;
    --sand: #c9b79a;
    --building: #b9c3cb;
  }
  * { margin: 0; padding: 0; box-sizing: border-box; }
  html, body {
    width: 1200px; height: 884px; overflow: hidden;
    background: var(--page-bg);
    font-family: "Raleway", Arial, sans-serif;
  }
  .card {
    position: absolute; left: 50px; top: 182px;
    width: 1100px; height: 519px;
    background: linear-gradient(180deg, var(--card-white) 55%, var(--card-fade) 100%);
    box-shadow: 0 14px 40px rgba(0,0,0,0.18);
    overflow: hidden;
  }
  .card__art { position: absolute; inset: 0; width: 1100px; height: 519px; }
  .brand {
    position: absolute; right: 48px; top: 238px;
    display: flex; align-items: center; gap: 14px;
  }
  .brand__dot { width: 26px; height: 26px; border-radius: 50%; background: var(--teal); }
  .brand__name {
    font-weight: 600; font-size: 30px; letter-spacing: 0.5px;
    color: var(--ink); text-transform: uppercase;
  }
  .greeting {
    position: absolute; left: 52px; top: 340px;
    font-weight: 600; font-size: 72px; letter-spacing: 1px;
    color: var(--teal); line-height: 1;
  }
  .contact {
    position: absolute; left: 54px; top: 420px;
    list-style: none; color: var(--teal);
    font-weight: 500; font-size: 20px; line-height: 27px;
  }
</style>
</head>
<body>
  <main class="card">
    <svg class="card__art" viewBox="0 0 1100 519">
      <defs>
        <linearGradient id="buildingsTone" x1="0" y1="0" x2="0" y2="1">
          <stop offset="0" stop-color="#d7e6ef"/>
          <stop offset="0.45" stop-color="#b9c3cb"/>
          <stop offset="1" stop-color="#7d8f5c"/>
        </linearGradient>
        <linearGradient id="beachTone" x1="0" y1="0" x2="0" y2="1">
          <stop offset="0" stop-color="#9fc6dc"/>
          <stop offset="0.55" stop-color="#2f6f95"/>
          <stop offset="1" stop-color="#c9b79a"/>
        </linearGradient>
        <linearGradient id="treeTone" x1="0" y1="0" x2="0" y2="1">
          <stop offset="0" stop-color="#6d7a52"/>
          <stop offset="0.6" stop-color="#8d7a5f"/>
          <stop offset="1" stop-color="#c9b79a"/>
        </linearGradient>
        <linearGradient id="bayTone" x1="0" y1="0" x2="0" y2="1">
          <stop offset="0" stop-color="#bcd8ea"/>
          <stop offset="0.5" stop-color="#3a7ea6"/>
          <stop offset="1" stop-color="#1f5c80"/>
        </linearGradient>
        <filter id="softShadow" x="-30%" y="-30%" width="160%" height="160%">
          <feDropShadow dx="0" dy="5" stdDeviation="6" flood-color="#000" flood-opacity="0.3"/>
        </filter>
      </defs>

      <path class="photo-band" role="img" aria-label="Photo of modern waterfront apartment buildings among trees"
            d="M0 0 H1100 V140 Q760 205 420 235 Q180 255 0 260 Z" fill="url(#buildingsTone)"/>
      <path class="photo-band__edge" d="M0 260 Q180 255 420 235 Q760 205 1100 140" fill="none" stroke="#fff" stroke-width="6"/>

      <g class="photo-circle" filter="url(#softShadow)">
        <circle cx="150" cy="262" r="66" fill="#fff"/>
        <circle cx="150" cy="262" r="58" fill="url(#beachTone)" role="img" aria-label="Photo of a beach with waves and sky"/>
      </g>
      <g class="photo-circle" filter="url(#softShadow)">
        <circle cx="375" cy="226" r="86" fill="#fff"/>
        <circle cx="375" cy="226" r="77" fill="url(#treeTone)" role="img" aria-label="Photo of a large shade tree beside a harbour beach"/>
      </g>
      <g class="photo-circle" filter="url(#softShadow)">
        <circle cx="640" cy="176" r="66" fill="#fff"/>
        <circle cx="640" cy="176" r="58" fill="url(#bayTone)" role="img" aria-label="Photo of boats moored in a calm bay"/>
      </g>
    </svg>

    <div class="brand">
      <span class="brand__dot"></span>
      <span class="brand__name">Harbour Lane Realty</span>
    </div>

    <h1 class="greeting">THANK YOU</h1>
    <ul class="contact">
      <li>Suite 6, 17 Wentmore Rd, Calderwood NSW 2187</li>
      <li>Tel: 0493 716 258</li>
      <li>Email: info@harbourlanerealty.com.au</li>
    </ul>
  </main>
</body>
</html>
```